Business Card Design Project

for a second hand vintage clothing store. shop name is The Velvet Cupboard

Cards to be double sided

The name on the card is Joanna Whitfield

Information to put on card:

The Velvet Cupboard
Joanna Whitfield (no job title)
42/871 Dunmore St, Glenwick, Sydney, NSW, 2009.
Mobile: 0412 905 261
Email: thevelvetcupboard@mailbox.com.au
Web: www.thevelvetcupboard.com.au

Target Market(s)

Women looking at vintage clothing

Industry/Entity Type

Clothing

```html
<!DOCTYPE html>
<html lang="en">
<head>
<meta charset="utf-8">
<title>The Velvet Cupboard – Business Card</title>
<link rel="stylesheet" href="https://fonts.googleapis.com/css2?family=Didact+Gothic&display=swap">
<style>
  :root {
    --page: #ffffff;
    --card: #000000;
    --label: #000000;
    --brand-gold: #e9d18c;
    --name-first: #ffffff;
    --name-last: #6b6b6b;
    --prefix-red: #8e1414;
    --detail: #ffffff;
    --detail-muted: #bdbdbd;
  }
  html, body {
    margin: 0;
    padding: 0;
    width: 1200px;
    height: 1200px;
    overflow: hidden;
    background: var(--page);
    font-family: "Didact Gothic", sans-serif;
  }
  .canvas {
    position: relative;
    width: 1200px;
    height: 1200px;
  }
  .side-label {
    position: absolute;
    left: 0;
    width: 1200px;
    text-align: center;
    font-size: 16px;
    color: var(--label);
  }
  .side-label--back { top: 46px; }
  .side-label--front { top: 546px; }

  .card {
    position: absolute;
    width: 881px;
    height: 441px;
    background: var(--card);
    overflow: hidden;
  }
  .card--back { left: 136px; top: 82px; }
  .card--front { left: 135px; top: 582px; }

  .brand-name {
    position: absolute;
    margin: 0;
    color: var(--brand-gold);
    font-weight: 400;
    white-space: nowrap;
    letter-spacing: 1px;
  }
  .card--back .brand-name {
    right: 58px;
    top: 52px;
    font-size: 40px;
  }
  .card--front .brand-name {
    right: 36px;
    top: 262px;
    font-size: 54px;
  }

  .holder-name {
    position: absolute;
    left: 42px;
    top: 236px;
    margin: 0;
    font-size: 33px;
    font-weight: 400;
    letter-spacing: 6px;
    white-space: nowrap;
  }
  .holder-name__first { color: var(--name-first); }
  .holder-name__last { color: var(--name-last); }

  .phone {
    position: absolute;
    left: 45px;
    top: 300px;
    font-size: 24px;
    letter-spacing: 5px;
    color: var(--detail);
    white-space: nowrap;
  }
  .phone__prefix { color: var(--prefix-red); }

  .contact-details {
    position: absolute;
    left: 45px;
    top: 348px;
    margin: 0;
    padding: 0;
    list-style: none;
    font-size: 15px;
    line-height: 23px;
    letter-spacing: 2px;
    color: var(--detail-muted);
    white-space: nowrap;
  }
</style>
</head>
<body>
  <main class="canvas">
    <div class="side-label side-label--back">Back side</div>
    <section class="card card--back" aria-label="Card back">
      <h2 class="brand-name">The Velvet Cupboard</h2>
      <h1 class="holder-name"><span class="holder-name__first">Joanna</span> <span class="holder-name__last">Whitfield</span></h1>
      <div class="phone"><span class="phone__prefix">(+61)</span>0412 905 261</div>
      <ul class="contact-details">
        <li class="contact-details__address">42/871 Dunmore St, Glenwick, Sydney, NSW, 2009</li>
        <li class="contact-details__email">thevelvetcupboard@mailbox.com.au</li>
        <li class="contact-details__web">www.thevelvetcupboard.com.au</li>
      </ul>
    </section>

    <div class="side-label side-label--front">Front side</div>
    <section class="card card--front" aria-label="Card front">
      <h2 class="brand-name">The Velvet Cupboard</h2>
    </section>
  </main>
</body>
</html>
```